Family business needs stationery redesign with new logo

Family owned company, established in 1987 wanting a brand 'refresh'. We are an electrical, refrigeration and construction company based in the Barkly Region Northern Territory, Australia. We have a new logo we would like to use which is uploaded along with our current letterhead and email signature. We are also dropping the word 'contractors' so please do not include this on any designs. Please note also, the 'orange' color used in our logo and designs should be Northern Territory red ochre which is as follows:

RGB (Hex): #C75B12
PantoneĀ® 159 C
CMYK: 1 / 74 / 100 / 7

We are needing our stationery redesigned using our new logo. Please include letterheads, business cards, envelopes, and email signatures.

We currently use our business letterheads for quotations, invoices, letters, HR matters, and internal memos.

We also need a separate simplified letterhead for internal paperwork such as employee leave forms, meeting agendas, and meeting minutes etc.
Updates

Reason: Needing more submissions of full package designs. We are wanting all our stationery, including business cards, letterheads, email signatures, envelopes, etc to be cohesive. We also require ALL the information, as supplied on our template letterhead, to be included on the new letterhead designs. including electrical license no.etc Thank you, K&M

Reason: needing more time as work has got in the way of looking over designs. A lot of designs not meeting the brief/criteria.

Industry/Entity Type

Business

Colors
0355a3
f37122

Requirements
Must have
• The 'orange' color used in the designs should be Northern Territory red ochre which is as follows:
• RGB (Hex): #C75B12
• PantoneĀ® 159 C
• CMYK: 1 / 74 / 100 / 7
• ***MUST INCLUDE ALL INFORMATION THAT IS ON OUR CURRENT LETTERHEAD***
Should not have
• Please do not include the word 'contractors'

```html
<!DOCTYPE html>
<html lang="en">
<head>
<meta charset="utf-8">
<title>K&amp;M Stationery Set</title>
<link rel="stylesheet" href="https://fonts.googleapis.com/css2?family=Poppins:wght@400;500;600;700&display=swap">
<style>
  :root {
    --ochre: #DE6220;
    --blue: #1B5BAA;
    --ink: #555555;
    --paper: #ffffff;
    --bg-center: #fbfbfb;
    --bg-edge: #d9d9d9;
    --window: #ececec;
  }
  * { margin: 0; padding: 0; box-sizing: border-box; }
  html, body { width: 1200px; height: 1200px; overflow: hidden; }
  body {
    position: relative;
    font-family: "Poppins", sans-serif;
    background: radial-gradient(circle at 50% 45%, var(--bg-center) 0%, var(--bg-edge) 100%);
  }
  .piece {
    position: absolute;
    background: var(--paper);
    box-shadow: 3px 4px 0 #8d8d8d, 4px 6px 10px rgba(0,0,0,.25);
    overflow: hidden;
  }
  .brand-name { font-weight: 700; color: var(--blue); line-height: 1; position: absolute; display: flex; align-items: center; gap: 4px; }
  .brand-dot { display: inline-block; border-radius: 50%; background: var(--blue); }
  .tagline { position: absolute; font-weight: 600; color: var(--ochre); white-space: nowrap; }
  .contact-list { position: absolute; list-style: none; color: var(--blue); }
  .contact-list li { display: flex; align-items: center; gap: 3px; white-space: nowrap; }
  .contact-list .icon { border: 1px solid currentColor; border-radius: 50%; flex: none; }

  /* Letterhead */
  .letterhead { left: 244px; top: 288px; width: 314px; height: 412px; }
  .letterhead .brand-name { left: 20px; top: 14px; font-size: 17px; }
  .letterhead .tagline { left: 18px; top: 38px; font-size: 4.5px; }
  .letterhead .divider { position: absolute; left: 113px; top: 12px; width: 1px; height: 36px; background: var(--blue); }
  .letterhead .contact-list { left: 118px; top: 13px; font-size: 3.6px; line-height: 5.6px; }
  .letterhead .contact-list .icon { width: 4px; height: 4px; }
  .letter-body { position: absolute; left: 18px; top: 122px; width: 280px; font-size: 6px; line-height: 9px; color: var(--ink); }
  .letter-body p { margin-bottom: 9px; }
  .letterhead .footer-band { position: absolute; left: 0; bottom: 0; width: 100%; height: 19px; background: var(--ochre); color: #fff; font-size: 5.5px; font-weight: 600; text-align: center; line-height: 19px; letter-spacing: .5px; }

  /* Envelope back */
  .envelope-back { left: 652px; top: 318px; width: 317px; height: 152px; }
  .envelope-back .flap { position: absolute; left: 0; top: 0; }
  .envelope-back .flap-name { position: absolute; left: 0; top: 5px; width: 100%; text-align: center; color: #fff; font-weight: 700; font-size: 9px; }

  /* Envelope front */
  .envelope-front { left: 652px; top: 523px; width: 317px; height: 156px; }
  .envelope-front .brand-name { left: 42px; top: 15px; font-size: 17px; }
  .envelope-front .tagline { left: 22px; top: 42px; font-size: 4.6px; }
  .envelope-front .contact-list { left: 22px; top: 65px; font-size: 7px; line-height: 9.6px; font-weight: 500; }
  .envelope-front .contact-list .icon { width: 6px; height: 6px; }
  .envelope-front .address-window { position: absolute; left: 202px; top: 97px; width: 85px; height: 30px; background: var(--window); border-radius: 4px; }
  .envelope-front .rule { position: absolute; left: 0; top: 138px; width: 100%; height: 3px; background: var(--ochre); }

  /* Email signature */
  .email-signature { left: 248px; top: 756px; width: 314px; height: 152px; }
  .email-signature .person-name { position: absolute; left: 43px; top: 13px; font-size: 12px; color: var(--blue); }
  .email-signature .person-title { position: absolute; left: 16px; top: 29px; font-size: 6px; color: var(--blue); }
  .email-signature .contact-list { left: 16px; top: 41px; font-size: 5.6px; line-height: 8.2px; }
  .email-signature .contact-list .icon { width: 5px; height: 5px; }
  .email-signature .divider { position: absolute; left: 160px; top: 12px; width: 1.5px; height: 82px; background: var(--blue); }
  .email-signature .brand-name { left: 235px; top: 30px; font-size: 17px; }
  .email-signature .tagline { left: 218px; top: 62px; font-size: 4.6px; }
  .email-signature .rule { position: absolute; left: 17px; top: 109px; width: 287px; height: 1.5px; background: var(--blue); }
  .follow-row { position: absolute; left: 17px; top: 127px; display: flex; align-items: center; gap: 12px; font-size: 7.5px; font-weight: 600; color: var(--blue); }
  .social-dot { width: 10px; height: 10px; border-radius: 50%; background: var(--ochre); display: inline-block; }
  .follow-row .dots { display: flex; gap: 12px; }

  /* Business cards */
  .card-front { left: 626px; top: 756px; width: 151px; height: 91px; background: var(--ochre); }
  .card-front .brand-name { left: 0; width: 100%; justify-content: center; top: 24px; font-size: 17px; color: #fff; }
  .card-front .brand-dot { background: #fff; }
  .card-front .tagline { left: 0; width: 100%; text-align: center; top: 52px; font-size: 5.2px; color: #fff; }
  .card-front .web { position: absolute; left: 0; width: 100%; text-align: center; top: 72px; font-size: 3.6px; color: #f7d3bd; letter-spacing: .4px; }

  .card-back { left: 806px; top: 756px; width: 152px; height: 91px; }
  .card-back .brand-name { left: 0; width: 100%; justify-content: center; top: 6px; font-size: 13px; }
  .card-back .tagline { left: 0; width: 100%; text-align: center; top: 27px; font-size: 3.6px; }
  .card-back .panel { position: absolute; left: 0; top: 38px; width: 100%; height: 53px; background: var(--ochre); color: #fff; }
  .card-back .person-name { position: absolute; left: 0; width: 100%; text-align: center; top: 2px; font-size: 7.5px; }
  .card-back .person-title { position: absolute; left: 0; width: 100%; text-align: center; top: 12px; font-size: 3.8px; }
  .card-back .contact-list { color: #fff; font-size: 3.3px; line-height: 5px; top: 20px; }
  .card-back .contact-list .icon { width: 3px; height: 3px; }
  .card-back .col-left { left: 18px; }
  .card-back .col-right { left: 92px; }
  .card-back .abn { position: absolute; left: 0; width: 100%; text-align: center; top: 43px; font-size: 3.4px; font-weight: 600; }
</style>
</head>
<body>

<section class="piece letterhead">
  <div class="brand-name">K&amp;M <span class="brand-dot" style="width:5px;height:5px"></span></div>
  <div class="tagline">Electrical - Refrigeration - Building Servis</div>
  <div class="divider"></div>
  <ul class="contact-list">
    <li><span class="icon"></span>PO Box 2240, 52 Hollis</li>
    <li>&nbsp;&nbsp;St Marlow NT 0870</li>
    <li><span class="icon"></span>08-5550-1234</li>
    <li><span class="icon"></span>08-5550-1234</li>
    <li><span class="icon"></span>@kmservices.com.au</li>
    <li><span class="icon"></span>www.kmservices.com.au</li>
  </ul>
  <div class="letter-body">
    <p>Dear [Recipient],</p>
    <p>We love the look of this stationery just the way it is. But you can add your own personal touch in almost no time.</p>
    <p>On the Design tab of the ribbon, check out the Themes, Colors, and Fonts galleries to preview different looks from a variety of choices. Then just click to apply the one you like.</p>
    <p>We've also created styles that let you match the formatting you see in this letter with just a click. On the Home tab of the ribbon, check out the Styles gallery for all styles used in this letter.</p>
    <p>Ready to add your digits? No problem. Just double click the header area to add your contact information.</p>
    <p style="margin-bottom:0">Warm regards,</p>
    <p>Jordan</p>
  </div>
  <div class="footer-band">ABN 00 000 000 000</div>
</section>

<section class="piece envelope-back">
  <svg class="flap" width="317" height="30" viewBox="0 0 317 30"><polygon points="0,0 317,0 308,30 9,30" fill="var(--ochre)"/></svg>
  <div class="flap-name">K&amp;M</div>
</section>

<section class="piece envelope-front">
  <div class="brand-name">K&amp;M <span class="brand-dot" style="width:5px;height:5px"></span></div>
  <div class="tagline">Electrical - Refrigeration - Building Servis</div>
  <ul class="contact-list">
    <li><span class="icon"></span>PO Box 2240, 52 Hollis</li>
    <li>&nbsp;&nbsp;&nbsp;St Marlow NT 0870</li>
    <li><span class="icon"></span>08-5550-1234</li>
    <li><span class="icon"></span>08-5550-1234</li>
    <li><span class="icon"></span>@kmservices.com.au</li>
    <li><span class="icon"></span>www.kmservices.com.au</li>
  </ul>
  <div class="address-window"></div>
  <div class="rule"></div>
</section>

<section class="piece email-signature">
  <div class="person-name">Dana</div>
  <div class="person-title">Corporate Service Manager</div>
  <ul class="contact-list">
    <li><span class="icon"></span>PO Box 2240, 52 Hollis</li>
    <li>&nbsp;&nbsp;&nbsp;St Marlow NT 0870</li>
    <li><span class="icon"></span>08-5550-1234</li>
    <li><span class="icon"></span>08-5550-1234</li>
    <li><span class="icon"></span>@kmservices.com.au</li>
    <li><span class="icon"></span>www.kmservices.com.au</li>
  </ul>
  <div class="divider"></div>
  <div class="brand-name">K&amp;M <span class="brand-dot" style="width:5px;height:5px"></span></div>
  <div class="tagline">Electrical - Refrigeration - Building Servis</div>
  <div class="rule"></div>
  <div class="follow-row">Follow us on:
    <span class="dots"><span class="social-dot"></span><span class="social-dot"></span><span class="social-dot"></span><span class="social-dot"></span></span>
  </div>
</section>

<section class="piece card-front">
  <div class="brand-name">K&amp;M <span class="brand-dot" style="width:5px;height:5px"></span></div>
  <div class="tagline">Electrical - Refrigeration - Building Servis</div>
  <div class="web">www.kmservices.com.au</div>
</section>

<section class="piece card-back">
  <div class="brand-name">K&amp;M <span class="brand-dot" style="width:4px;height:4px"></span></div>
  <div class="tagline">Electrical - Refrigeration - Building Servis</div>
  <div class="panel">
    <div class="person-name">Dana</div>
    <div class="person-title">Corporate Service Manager</div>
    <ul class="contact-list col-left">
      <li><span class="icon"></span>PO Box 2240, 52 Hollis</li>
      <li>&nbsp;&nbsp;St Marlow NT 0870</li>
      <li><span class="icon"></span>08-5550-1234</li>
    </ul>
    <ul class="contact-list col-right">
      <li><span class="icon"></span>08-5550-1234</li>
      <li><span class="icon"></span>@kmservices.com.au</li>
      <li><span class="icon"></span>www.kmservices.com.au</li>
    </ul>
    <div class="abn">ABN 00 000 000 000</div>
  </div>
</section>

</body>
</html>
```